Willow Dental Business Card

We need business cards for our dental office.
We are looking for a clean, elegant design

We provide dental services to children.
Our card needs to be appealing to referring dentists, parents and our team

Target Market(s)

referring dentists, parents and our team

Industry/Entity Type

Dental Clinic

Contact Information for Business Card

4856 Fenwick Lane, Suite 240
Brookhaven Falls, WI 53811

608-382-7461 Voice
608-382-7469 fax
info@willowdentalco.com email
www.willowdentalco.com web

Font styles to use
Sans Serif

Requirements
Must have
• White background - clean, crisp, elegant, simple
• rounded corners
• different color palate - once we come up with design, we will replace the blue with orange, green,
Nice to have
• Follow our logo typeface and colors
• then we can replace color

```html
<!DOCTYPE html>
<html lang="en">
<head>
<meta charset="utf-8">
<title>Willow Dental Business Card</title>
<link href="https://fonts.googleapis.com/css2?family=Open+Sans:wght@400;600;700&display=swap" rel="stylesheet">
<style>
  :root {
    --brand-blue: #12a8e6;
    --brand-blue-deep: #0c97d4;
    --paper-white: #ffffff;
    --paper-shade: #eef1f3;
    --ink-white: #ffffff;
    --page-bg: #e4e6e8;
  }
  * { margin: 0; padding: 0; box-sizing: border-box; }
  html, body {
    width: 1200px; height: 1000px; overflow: hidden;
    background: var(--page-bg);
    font-family: "Open Sans", Arial, sans-serif;
  }
  .card {
    position: absolute;
    left: 250px;
    width: 700px; height: 400px;
    border-radius: 26px;
    overflow: hidden;
    box-shadow: 0 6px 18px rgba(0,0,0,0.12);
  }
  /* back side */
  .card-back {
    top: 60px;
    background: linear-gradient(160deg, var(--brand-blue) 0%, var(--brand-blue-deep) 100%);
    color: var(--ink-white);
    display: flex; flex-direction: column; align-items: center; justify-content: center;
  }
  .back-wordmark {
    display: flex; align-items: center; gap: 16px;
    font-weight: 600; font-size: 46px; letter-spacing: 0.5px;
  }
  .wordmark-dot {
    width: 30px; height: 30px; border-radius: 50%;
    background: var(--ink-white);
    flex: none;
  }
  .back-web {
    margin-top: 70px;
    font-size: 20px; letter-spacing: 2px;
  }
  /* front side */
  .card-front {
    top: 540px;
    background: var(--brand-blue);
  }
  .front-panel {
    position: absolute; inset: 0;
  }
  .holder {
    position: absolute; left: 44px; top: 40px;
    color: var(--ink-white);
  }
  .holder-name { font-weight: 700; font-size: 24px; line-height: 1.1; }
  .holder-title { font-size: 16px; }
  .contact {
    position: absolute; left: 44px; top: 178px;
    color: var(--ink-white); font-size: 17px; line-height: 25px;
    list-style: none;
  }
  .contact li { display: flex; align-items: center; gap: 8px; white-space: nowrap; }
  .contact svg { width: 15px; height: 15px; flex: none; }
  .front-wordmark {
    position: absolute; left: 365px; top: 0; width: 320px; height: 400px;
    display: flex; align-items: center; justify-content: center; gap: 10px;
    color: var(--brand-blue);
    font-weight: 600; font-size: 32px; white-space: nowrap;
  }
  .front-wordmark .wordmark-dot { width: 18px; height: 18px; background: var(--brand-blue); }
</style>
</head>
<body>

<section class="card card-back" aria-label="Card back">
  <div class="back-wordmark"><span class="wordmark-dot"></span>Willow Dental</div>
  <div class="back-web">www.willowdentalco.com</div>
</section>

<section class="card card-front" aria-label="Card front">
  <svg class="front-panel" viewBox="0 0 700 400" aria-hidden="true">
    <defs>
      <linearGradient id="paperFade" x1="0" y1="0" x2="0" y2="1">
        <stop offset="0" stop-color="#ffffff"/>
        <stop offset="1" stop-color="#eef1f3"/>
      </linearGradient>
    </defs>
    <path d="M430 0 C 360 60, 340 160, 352 240 C 362 310, 390 360, 420 400 L 700 400 L 700 0 Z" fill="url(#paperFade)"/>
    <path d="M430 0 C 360 60, 340 160, 352 240 C 362 310, 390 360, 420 400" fill="none" stroke="#cfe9f6" stroke-width="8"/>
  </svg>

  <div class="holder">
    <div class="holder-name">Nora Whitfield</div>
    <div class="holder-title">President</div>
  </div>

  <ul class="contact">
    <li>4856 Fenwick Lane, Suite 240</li>
    <li>Brookhaven Falls, WI 53811</li>
    <li>
      <svg viewBox="0 0 16 16"><path fill="#fff" d="M2 6c0-2 2-3 6-3s6 1 6 3v1h-3V5.5H5V7H2z M4 8h8l1 6H3z"/><circle cx="8" cy="11" r="1.6" fill="#12a8e6"/></svg>
      608-382-7461
    </li>
    <li>
      <svg viewBox="0 0 16 16"><rect x="4" y="1" width="8" height="5" fill="#fff"/><rect x="1" y="6" width="14" height="8" rx="1.5" fill="#fff"/><rect x="4" y="9" width="8" height="2" fill="#12a8e6"/></svg>
      608-382-7469
    </li>
    <li>
      <svg viewBox="0 0 16 16"><rect x="1" y="3" width="14" height="10" fill="#fff"/><path d="M1 3l7 6 7-6" fill="none" stroke="#12a8e6" stroke-width="1.3"/></svg>
      info@willowdentalco.com
    </li>
    <li>
      <svg viewBox="0 0 16 16"><circle cx="8" cy="8" r="7" fill="#fff"/><path d="M8 1v14M1 8h14M3 4.5h10M3 11.5h10" stroke="#12a8e6" stroke-width="1"/></svg>
      www.willowdentalco.com
    </li>
  </ul>

  <div class="front-wordmark"><span class="wordmark-dot"></span>Willow Dental</div>
</section>

</body>
</html>
```